TalkBridge - Language Coaching Services

Sleek, innovative, trendy design for Language Coaching business.

TalkBridge is a new UK based company that provides Language Coaching services. We offer highly personalized on-line and face to face language courses. We also impart learning techniques workshops based on the latest neuroscience research for second-language acquisition.

Target Market(s)

Industry/Entity Type

Consulting

Contact Information for Business Card

TalkBridge
ElenaVT@talkbridge-demo.co.uk
TalkBridge-demo.co.uk
London, UK

Font styles to use
Sans Serif

```html
<!DOCTYPE html>
<html lang="en">
<head>
<meta charset="utf-8">
<title>TalkBridge Business Card</title>
<link rel="stylesheet" href="https://fonts.googleapis.com/css2?family=Montserrat:wght@400&family=Open+Sans:wght@400;700&display=swap">
<style>
  :root {
    --backdrop: #e9ecee;
    --paper: #ffffff;
    --brand-light: #2a8fb6;
    --brand-dark: #1b5b82;
    --brand-mid: #1f78a3;
    --ink: #4a4f54;
    --shadow: rgba(20, 30, 40, 0.25);
  }
  * { box-sizing: border-box; margin: 0; padding: 0; }
  html, body {
    width: 1200px; height: 1000px; overflow: hidden;
    background: var(--backdrop);
  }
  .canvas { position: relative; width: 1200px; height: 1000px; }

  .card {
    position: absolute; left: 267px; width: 663px; height: 396px;
    box-shadow: 0 6px 16px var(--shadow);
  }
  .card--front {
    top: 73px; background: var(--paper);
    border-radius: 22px 198px 198px 22px / 22px 198px 198px 22px;
  }
  .card--back {
    top: 534px;
    background: linear-gradient(90deg, var(--brand-light) 0%, var(--brand-mid) 55%, var(--brand-dark) 100%);
    border-radius: 198px 22px 22px 198px / 198px 22px 22px 198px;
  }

  .wordmark {
    position: absolute;
    font-family: "Montserrat", sans-serif; font-weight: 400;
    letter-spacing: 1px; white-space: nowrap; line-height: 1;
  }
  .card--front .wordmark { left: 31px; top: 58px; font-size: 37px; color: var(--brand-mid); }
  .card--back .wordmark { left: 396px; top: 182px; font-size: 33px; color: var(--paper); }

  .brand-disc { position: absolute; border-radius: 50%; }
  .card--front .brand-disc {
    left: 299px; top: 32px; width: 332px; height: 332px;
    background: radial-gradient(circle at 35% 35%, var(--brand-light), var(--brand-dark));
  }
  .card--back .brand-disc {
    left: 35px; top: 35px; width: 326px; height: 326px;
    background: radial-gradient(circle at 40% 40%, rgba(255,255,255,0.95), rgba(255,255,255,0.8));
  }

  .contact {
    position: absolute; left: 32px; top: 168px;
    font-family: "Open Sans", sans-serif; color: var(--ink);
  }
  .contact__name { font-weight: 700; font-size: 20px; color: var(--brand-mid); letter-spacing: 0.3px; line-height: 24px; }
  .contact__title { font-size: 15.5px; line-height: 22px; }
  .contact__address { margin-top: 18px; font-size: 15.5px; line-height: 21px; }
  .contact__list { list-style: none; margin-top: 10px; font-size: 15px; line-height: 21px; }
  .contact__list li { display: flex; align-items: center; gap: 6px; }
  .contact__icon { width: 15px; height: 15px; fill: var(--brand-mid); flex: none; }
</style>
</head>
<body>
<main class="canvas">

  <section class="card card--front" aria-label="Card front">
    <div class="wordmark">TALKBRIDGE</div>
    <div class="contact">
      <p class="contact__name">NORA LINDQVIST</p>
      <p class="contact__title">Cheif Managing Officer</p>
      <p class="contact__address">18 Harrow Lane, Suite 4<br>London, UK</p>
      <ul class="contact__list">
        <li>
          <svg class="contact__icon" viewBox="0 0 16 16" aria-hidden="true"><path d="M1 5c0-2 3-3 7-3s7 1 7 3v1h-4V5H5v1H1z"/><path d="M3 7h10l1 6H2z"/></svg>
          + 000 000 0000
        </li>
        <li>
          <svg class="contact__icon" viewBox="0 0 16 16" aria-hidden="true"><rect x="4" y="1" width="8" height="4"/><rect x="1" y="6" width="14" height="6" rx="1"/><rect x="4" y="10" width="8" height="5"/></svg>
          + 000 000 0000
        </li>
        <li>
          <svg class="contact__icon" viewBox="0 0 16 16" aria-hidden="true"><rect x="1" y="3" width="14" height="10" rx="1"/><path d="M1.5 3.5 8 9l6.5-5.5" stroke="#fff" stroke-width="1.3" fill="none"/></svg>
          info@talkbridge-demo.co.uk
        </li>
        <li>
          <svg class="contact__icon" viewBox="0 0 16 16" aria-hidden="true"><circle cx="8" cy="8" r="7"/><path d="M1 8h14M8 1c-3 3-3 11 0 14M8 1c3 3 3 11 0 14" stroke="#fff" stroke-width="1" fill="none"/></svg>
          www.talkbridge-demo.co.uk
        </li>
      </ul>
    </div>
    <div class="brand-disc" role="img" aria-label="Brand symbol area: circular emblem in blue tones"></div>
  </section>

  <section class="card card--back" aria-label="Card back">
    <div class="brand-disc" role="img" aria-label="Brand symbol area: circular emblem in white"></div>
    <div class="wordmark">TALKBRIDGE</div>
  </section>

</main>
</body>
</html>
```